Real Estate Agent need a business card

I am a real estate agent in Vancouver, BC Canada. I recently used PixelHarbor to develop a logo of my own. I would like to have my logo in the business card, as well my realty office logo also must be displayed along with its address. I also would like to have my headshot photo displayed in the business card on both sides.

Industry/Entity Type

Real Estate Agent

Contact Information for Business Card

My office address:
Bramwell Peak Realty
2271 Lindqvist St.
Vancouver, BC V5K 2P8

My contact information:
Cell: 604-555-0148
Office: 604-555-0192
Fax: 604-555-0193

My website : www.danielmorvik.example
My email: email@danielmorvik.example

My slogan: Honest work. Always Further.

Requirements
Must have
• Front side(all in colour): My photo, My own logo, My office logo, My cell number, My website address and email, My slogan.
• Back side(could be black & white/ plz refer to the file name "preview"): My photo, My own logo, my office logo, my office address, my contact information.
• * Please read this: Since my logo has my name in it, there is no need to put my name in the card separately. As well, my office logo MUST BE displayed on both sides(you can reduce the size of office logo). But the office address can be displayed only one side, front or back. I would prefer to have my cell number only to be displayed prominently on the front side. So all the numbers should be displayed on the backside instead. Remember that I am trying to promote myself so the most important thing I consider from the front side of the card is my cell number, my website, and my email, not the office. The only thing I require by industry regulation from the front side is my office logo. Hope this helps.
Nice to have
• Colour on the front side and the black and white on the back side

```html
<!DOCTYPE html>
<html lang="en">
<head>
<meta charset="utf-8">
<title>Daniel Morvik – Business Card</title>
<link rel="stylesheet" href="https://fonts.googleapis.com/css2?family=Montserrat:wght@600;700&family=Source+Sans+3:wght@400;600&display=swap">
<style>
  :root {
    --page: #e9e9e9;
    --card: #ffffff;
    --ink: #4a4a4c;
    --text: #3c3c3e;
    --green: #7dc243;
    --band-dark: #4a4a4c;
    --photo-front-a: #3a4250;
    --photo-front-b: #c9ccd1;
    --photo-back-a: #6e6e6e;
    --photo-back-b: #d6d6d6;
  }
  * { box-sizing: border-box; margin: 0; padding: 0; }
  html, body { width: 1200px; height: 1000px; overflow: hidden; }
  body { background: var(--page); position: relative; font-family: "Source Sans 3", "Myriad Pro", sans-serif; color: var(--text); }

  .card { position: absolute; left: 265px; width: 665px; height: 397px; background: var(--card); overflow: hidden; box-shadow: 0 2px 8px rgba(0,0,0,.18); }
  .card--front { top: 73px; }
  .card--back { top: 533px; background: linear-gradient(115deg, #ffffff 30%, #ededed 75%, #f4f4f4 100%); }

  .agent-mark { position: absolute; left: 33px; width: 272px; text-align: center; }
  .agent-mark__name { display: block; font-family: "Montserrat", sans-serif; font-weight: 700; font-size: 29px; line-height: 34px; color: var(--ink); letter-spacing: .3px; white-space: nowrap; }
  .agent-mark__role { display: block; font-family: "Montserrat", sans-serif; font-weight: 600; font-size: 14px; line-height: 18px; color: var(--green); letter-spacing: 2.2px; white-space: nowrap; }
  .card--front .agent-mark { top: 135px; }
  .card--back .agent-mark { top: 125px; }

  .contact-list { position: absolute; left: 33px; list-style: none; font-size: 16.5px; }
  .contact-list li { display: flex; align-items: center; gap: 7px; height: 22.5px; white-space: nowrap; }
  .contact-list svg { width: 14px; height: 14px; flex: none; }
  .card--front .contact-list { top: 216px; }
  .card--front .contact-list li { height: 24px; }
  .card--back .contact-list { top: 281px; }
  .contact-list .accent { color: var(--green); }

  .office-address { position: absolute; left: 33px; top: 297px; font-size: 16.5px; line-height: 22px; font-style: normal; }
  .office-address strong { font-weight: 600; }

  .office-mark { position: absolute; width: 122px; text-align: center; font-weight: 600; font-size: 13px; line-height: 16px; color: var(--text); }
  .card--front .office-mark { left: 212px; top: 311px; }
  .card--back .office-mark { left: 33px; top: 221px; }

  .headshot { position: absolute; }
  .card--front .headshot { left: 375px; top: 50px; width: 270px; height: 318px; background: linear-gradient(180deg, var(--photo-front-b) 0%, var(--photo-front-a) 45%, var(--photo-front-a) 100%); border-radius: 120px 120px 0 0; }
  .card--back .headshot { left: 340px; top: 52px; width: 295px; height: 345px; background: linear-gradient(180deg, var(--photo-back-b) 0%, var(--photo-back-a) 45%, #5a5a5a 100%); border-radius: 130px 130px 0 0; }

  .signature-band { position: absolute; left: 340px; top: 310px; width: 325px; height: 58px; background: rgba(255,255,255,.55); }

  .base-band { position: absolute; left: 0; top: 379px; width: 330px; height: 18px; background: var(--band-dark); clip-path: polygon(0 0, 100% 0, 95% 100%, 0 100%); }
  .slogan-band { position: absolute; left: 315px; top: 365px; width: 350px; height: 32px; background: var(--green); clip-path: polygon(10% 0, 100% 0, 100% 100%, 0 100%); display: flex; align-items: center; justify-content: flex-end; padding-right: 27px; }
  .slogan-band p { color: #fff; font-size: 16.5px; white-space: nowrap; }
</style>
</head>
<body>

<section class="card card--front">
  <div class="agent-mark">
    <span class="agent-mark__name">DANIEL MORVIK</span>
    <span class="agent-mark__role">REAL ESTATE AGENT</span>
  </div>

  <ul class="contact-list">
    <li><svg viewBox="0 0 14 14"><rect x="3.5" y="0.5" width="7" height="13" rx="1.5" fill="var(--green)"/><rect x="5" y="2.5" width="4" height="7" fill="#fff"/></svg><span>604-555-0148</span></li>
    <li><svg viewBox="0 0 14 14"><rect x="0.5" y="3" width="13" height="9" fill="var(--green)"/><path d="M1 3.5 L7 8 L13 3.5" stroke="#fff" stroke-width="1.2" fill="none"/></svg><span>email@danielmorvik.example</span></li>
    <li><svg viewBox="0 0 14 14"><circle cx="7" cy="7" r="6" fill="var(--green)"/><path d="M1 7h12M7 1c-2.5 3-2.5 9 0 12M7 1c2.5 3 2.5 9 0 12" stroke="#fff" stroke-width="1" fill="none"/></svg><span>www.danielmorvik.example</span></li>
  </ul>

  <address class="office-address">
    <strong>Bramwell Peak Realty</strong><br>
    2271 Lindqvist St.<br>
    Vancouver, BC V5K 2P8
  </address>

  <p class="office-mark">Bramwell Peak<br>Realty</p>

  <div class="headshot" role="img" aria-label="Colour headshot of the agent in a dark suit and light shirt"></div>

  <div class="base-band"></div>
  <div class="slogan-band"><p>Honest work. Always Further.</p></div>
</section>

<section class="card card--back">
  <div class="agent-mark">
    <span class="agent-mark__name">DANIEL MORVIK</span>
    <span class="agent-mark__role">REAL ESTATE AGENT</span>
  </div>

  <p class="office-mark">Bramwell Peak<br>Realty</p>

  <ul class="contact-list">
    <li><svg viewBox="0 0 14 14"><path d="M1 6c0-3 12-3 12 0v1H10V5.5H4V7H1z" fill="var(--ink)"/><rect x="3" y="7.5" width="8" height="5" rx="1" fill="var(--ink)"/></svg><span>604-555-0192</span></li>
    <li><svg viewBox="0 0 14 14"><rect x="3.5" y="1" width="7" height="4" fill="var(--ink)"/><rect x="1" y="5" width="12" height="6" rx="1" fill="var(--ink)"/><rect x="3.5" y="9" width="7" height="4" fill="#fff" stroke="var(--ink)"/></svg><span>604-555-0192</span></li>
    <li><svg viewBox="0 0 14 14"><rect x="0.5" y="3" width="13" height="9" fill="var(--ink)"/><path d="M1 3.5 L7 8 L13 3.5" stroke="#fff" stroke-width="1.2" fill="none"/></svg><span>email@danielmorvik.example</span></li>
    <li><svg viewBox="0 0 14 14"><circle cx="7" cy="7" r="6" fill="var(--ink)"/><path d="M1 7h12M7 1c-2.5 3-2.5 9 0 12M7 1c2.5 3 2.5 9 0 12" stroke="#fff" stroke-width="1" fill="none"/></svg><span>www.<span class="accent">danielmorvik</span>.example</span></li>
  </ul>

  <div class="headshot" role="img" aria-label="Black and white headshot of the agent in a suit"></div>
  <div class="signature-band" role="img" aria-label="Light band carrying the agent's handwritten signature"></div>
</section>

</body>
</html>
```